Corporate Brochure Design for Cyber Resilience Solution (A4 PDF, 4 pages)

We are looking for a high-calibre designer to create a 4-page A4 PDF brochure promoting our digital resilience solution, Halcrest, and our company, DLO Dunmere Ledger Orbis. The design must reflect a premium, boardroom-ready style, as it is primarily shared with senior leaders in regulated financial services.
DLO Dunmere Ledger Orbis is a strategic advisory firm helping leadership teams achieve digital operational resilience. We combine board-level advisory, executive education, and a proprietary SaaS platform — Halcrest — to deliver cyber governance and compliance at scale.
Website: www.dlorbis.ie
Design Goals:
Target audience: C-level executives, particularly in financial services
Purpose: To instil confidence in our company and solution following an initial meeting
Style: Clean, modern, and corporate premium (5-star quality)
Tone: Strategic and authoritative
Format: A4 PDF (approx. 4 pages)
Visuals: Designer to select from provided Halcrest screenshots and align with overall layout
Continuity: Should visually complement our website and internal reports (Photoshop report templates provided for reference)
Content Provided:
Finalised brochure text (Microsoft Word format)
Logos for DLO and Halcrest
A folder of screenshots from our platform
Two Photoshop files used for internal reports (style inspiration)
Brochure Sections to Design:
Cover Page
Logo, strong visual brand, compelling title or tagline
Executive Summary / Who We Are
Introduce DLO and our flagship platform, Halcrest
What We Offer / How We Work With Clients
Break down our Steady Keel Programme and 4-phase engagement model
Use Cases & Contact
Highlight regulated sector experience and encourage next steps
Visual Direction:
Visual hierarchy must support strategic messaging
Include selected Halcrest platform screenshots where appropriate
Use consistent font and colour palette based on provided templates and site
Clean, uncluttered layout with room to breathe — not dense or technical
Deliverables:
4-page print-ready PDF
Source files (InDesign preferred)
Web-optimised PDF version
Any non-standard fonts or licences used
financial sector senior level

```html
<!DOCTYPE html>
<html lang="en">
<head>
<meta charset="utf-8">
<title>Halcrest Executive Report – Brochure Pages</title>
<link href="https://fonts.googleapis.com/css2?family=Montserrat:wght@500;600;700;800&family=Open+Sans:wght@400;600;700&display=swap" rel="stylesheet">
<style>
:root{
  --red:#d0121b;
  --red-dark:#8e0a10;
  --ink:#1c1c22;
  --panel:#3a3b40;
  --grey:#6b6d73;
  --paper:#ffffff;
  --paper-soft:#f3f3f4;
  --night:#0c0f1c;
  --night-2:#1d2538;
  --green:#2f9e4b;
  --amber:#e0bd2e;
  --bg:#e8e4df;
}
*{box-sizing:border-box;margin:0;padding:0}
html,body{width:1200px;height:900px;overflow:hidden;background:var(--bg)}
body{font-family:"Open Sans",Arial,sans-serif;color:var(--ink);position:relative}
.page{position:absolute;top:252px;width:280px;height:396px;background:var(--paper);overflow:hidden;box-shadow:0 6px 18px rgba(0,0,0,.18)}
.head{font-family:"Montserrat",Arial,sans-serif}

/* Cover */
.cover{left:20px}
.cover__block{position:absolute;left:0;top:44px;width:78px;height:58px;background:var(--red)}
.cover__image{position:absolute;left:40px;top:68px;width:200px;height:262px;background:radial-gradient(circle at 55% 78%,#120204 0,#3b0508 30%,#8d1118 62%,#5a0a0e 100%)}
.cover__band{position:absolute;left:178px;top:214px;width:102px;height:78px;background:var(--red);mix-blend-mode:multiply;opacity:.9}
.cover__title{position:absolute;left:24px;top:160px;color:#fff;font-family:"Montserrat",Arial,sans-serif;font-weight:800;font-size:33px;line-height:.98;letter-spacing:.5px;text-shadow:0 2px 6px rgba(0,0,0,.5)}
.brand{position:absolute;display:flex;align-items:center;gap:6px;font-family:"Montserrat",Arial,sans-serif;font-weight:700}
.brand__mark{width:9px;height:9px;border-radius:50%;background:var(--red)}
.brand__divider{width:1px;height:14px;background:currentColor;opacity:.5}
.cover .brand{right:20px;top:36px;font-size:9px;color:var(--ink)}
.cover__url{position:absolute;left:0;right:0;bottom:22px;text-align:center;font-size:8px;color:var(--ink)}

/* Spread */
.spread-left{left:320px;background:var(--paper-soft)}
.spread-right{left:600px;background:var(--paper)}
.spread-left::after{content:"";position:absolute;right:0;top:0;width:14px;height:100%;background:linear-gradient(90deg,transparent,rgba(0,0,0,.08))}
.label{position:absolute;display:flex;font-family:"Montserrat",Arial,sans-serif;font-weight:700;font-size:7px;color:#fff;text-transform:uppercase}
.label span{padding:2px 4px}
.label .lead{background:var(--red)}
.label .rest{background:var(--red-dark)}
.label .rest--dark{background:var(--panel)}
.body-copy{position:absolute;font-size:5.4px;line-height:1.45;color:var(--grey)}
.chart-card{position:absolute;left:20px;width:244px;background:#fff;border:1px solid #e2e2e4}
.chart-card__title{font-size:4.6px;color:var(--grey);padding:4px 6px}
.bars{display:flex;align-items:flex-end;gap:9px;height:56px;padding:0 14px 0 30px}
.bar{width:11px;display:flex;flex-direction:column}
.bar i{display:block}
.g{background:var(--green)}.a{background:var(--amber)}.r{background:var(--red)}
.bar-labels{display:flex;gap:9px;padding:3px 14px 4px 30px;font-size:3.6px;color:var(--grey)}
.bar-labels span{width:11px;text-align:center}
.chart-note{font-size:3.8px;color:var(--grey);text-align:center;padding-bottom:4px}
.phase-row{position:absolute;left:20px;top:276px;display:flex;gap:4px}
.phase{width:58px;height:74px;background:var(--panel);color:#ddd;font-size:4.8px;line-height:1.4;text-align:center;padding:5px 3px}
.phase b{display:block;color:var(--red);font-family:"Montserrat",Arial,sans-serif;font-size:4.8px;font-weight:700;text-transform:uppercase;margin-bottom:3px}
.edu-bar{position:absolute;left:20px;top:356px;width:244px;height:16px;background:var(--red);color:#fff;font-family:"Montserrat",Arial,sans-serif;font-weight:600;font-size:5.4px;text-align:center;line-height:16px;text-transform:uppercase}
.page-num{position:absolute;bottom:8px;width:11px;height:8px;background:var(--red);color:#fff;font-size:4.6px;text-align:center;line-height:8px}

.dora{position:absolute;left:16px;top:68px;width:248px;height:92px;background:#fff;border:1px solid #e2e2e4;padding:5px 6px}
.dora__org{display:flex;align-items:center;gap:4px;font-size:4.6px;color:var(--grey)}
.dora__org b{font-family:"Montserrat",Arial,sans-serif;color:#233a7a;font-size:5px}
.dora__sq{width:6px;height:6px;background:#233a7a}
.radars{display:flex;gap:6px;margin-top:6px}
.score{position:absolute;font-size:4px;padding:1px 3px;border:1px solid var(--amber);background:#fff6cf;color:var(--ink)}
.pill{position:absolute;left:64px;top:190px;width:156px;height:12px;border-radius:6px;background:var(--red);color:#fff;font-family:"Montserrat",Arial,sans-serif;font-weight:700;font-size:5px;text-align:center;line-height:12px;text-transform:uppercase}
.clients{position:absolute;left:24px;top:220px;width:236px;display:flex;flex-wrap:wrap;gap:5px 9px;font-family:"Open Sans",Arial,sans-serif;font-weight:700;font-size:8px;color:#2a2a30}
.corner{position:absolute;left:0;bottom:0}

/* Back */
.back{left:900px;background:linear-gradient(135deg,var(--night) 0%,#0a0d18 45%,var(--night-2) 70%,#070910 100%)}
.back .brand{left:50%;top:168px;transform:translateX(-50%);color:#fff;font-size:12px;gap:8px}
.back .brand__mark{width:12px;height:12px}
.contact{position:absolute;right:18px;top:238px;width:230px;text-align:right;color:#cfd3dc;font-size:5px;line-height:1.6}
.contact__title{font-family:"Montserrat",Arial,sans-serif;font-weight:700;color:var(--red);font-size:7px;text-transform:uppercase;border-bottom:1px solid var(--red);padding-bottom:3px;margin-bottom:5px}
.contact strong{color:#fff;font-weight:700}
</style>
</head>
<body>

<!-- Page 1: cover -->
<section class="page cover">
  <div class="cover__block"></div>
  <div class="brand"><span class="brand__mark"></span>DLO<span class="brand__divider"></span>HALCREST</div>
  <div class="cover__image" role="img" aria-label="Hooded figure with raised hands before a red wall of binary code"></div>
  <div class="cover__band"></div>
  <h1 class="cover__title">EXECUTIVE<br>REPORT</h1>
  <p class="cover__url">www.dlorbis.ie</p>
</section>

<!-- Page 2: who we are / how we work -->
<section class="page spread-left">
  <div class="label" style="left:20px;top:26px"><span class="lead">Who</span><span class="rest">We Are</span></div>
  <p class="body-copy" style="left:20px;top:40px;width:244px">Founded in 2014 by globally recognised cybersecurity leader Martin R Oakes, DLO Dunmere Ledger Orbis blends strategic advisory, executive education, and advanced technology to support organisations in regulated and high-risk sectors.</p>

  <div class="chart-card" style="top:68px">
    <p class="chart-card__title">NIS2 Compliance Across Key Areas</p>
    <div class="bars">
      <div class="bar"><i class="r" style="height:8px"></i><i class="a" style="height:6px"></i><i class="g" style="height:30px"></i></div>
      <div class="bar"><i class="r" style="height:10px"></i><i class="a" style="height:4px"></i><i class="g" style="height:28px"></i></div>
      <div class="bar"><i class="r" style="height:6px"></i><i class="a" style="height:8px"></i><i class="g" style="height:30px"></i></div>
      <div class="bar"><i class="r" style="height:12px"></i><i class="a" style="height:5px"></i><i class="g" style="height:30px"></i></div>
      <div class="bar"><i class="r" style="height:8px"></i><i class="a" style="height:10px"></i><i class="g" style="height:32px"></i></div>
      <div class="bar"><i class="r" style="height:14px"></i><i class="a" style="height:6px"></i><i class="g" style="height:31px"></i></div>
      <div class="bar"><i class="r" style="height:16px"></i><i class="a" style="height:6px"></i><i class="g" style="height:30px"></i></div>
      <div class="bar"><i class="r" style="height:9px"></i><i class="a" style="height:4px"></i><i class="g" style="height:40px"></i></div>
      <div class="bar"><i class="r" style="height:12px"></i><i class="a" style="height:7px"></i><i class="g" style="height:35px"></i></div>
    </div>
    <div class="bar-labels"><span>Gov</span><span>Risk</span><span>Ops</span><span>Supply</span><span>Asset</span><span>Access</span><span>Crypto</span><span>Event</span><span>Recov</span></div>
    <p class="chart-note">Status across each NIS2 area, with key gaps highlighted.</p>
  </div>

  <div class="chart-card" style="top:164px;height:100px">
    <p class="chart-card__title">Overall NIS2 Compliance Summary</p>
    <svg width="244" height="80" viewBox="0 0 244 80" role="img" aria-label="Pie chart of overall compliance: compliant, partial and gap">
      <path d="M122 38 L122 10 A28 28 0 1 1 97.5 51.6 Z" fill="var(--green)"/>
      <path d="M122 38 L97.5 51.6 A28 28 0 0 1 99 22 Z" fill="var(--red)"/>
      <path d="M122 38 L99 22 A28 28 0 0 1 122 10 Z" fill="var(--amber)"/>
      <text x="136" y="42" font-size="4" fill="#fff">Compliant</text>
      <text x="100" y="40" font-size="4" fill="#fff">Gap</text>
      <text x="88" y="16" font-size="3.8" fill="#6b6d73">Partial</text>
      <text x="122" y="76" font-size="3.8" fill="#6b6d73" text-anchor="middle">Overall view of the entity's NIS2 compliance position.</text>
    </svg>
  </div>

  <div class="label" style="left:20px;top:256px"><span class="lead">How</span><span class="rest rest--dark">We Work With Clients</span></div>
  <p class="body-copy" style="left:20px;top:268px">Our proven four-phase engagement model includes:</p>
  <div class="phase-row" style="top:278px">
    <div class="phase"><b>Initial Discovery &amp; Baseline Assessment</b>We contextualise your risk posture and identify regulatory and operational exposures.</div>
    <div class="phase"><b>Platform Deployment &amp; Enablement</b>We configure and onboard Halcrest, enabling full visibility and role-specific access.</div>
    <div class="phase"><b>Ongoing Strategic Advisory (vCISO Model)</b>Your dedicated advisor drives governance, compliance alignment, and incident readiness.</div>
    <div class="phase"><b>Maturity Reporting &amp; Board Briefings</b>We provide scheduled, digestible reporting for leadership and regulators.</div>
  </div>
  <div class="edu-bar">Embedded Executive Education</div>
  <div class="page-num" style="right:16px">02</div>
</section>

<!-- Page 3: reporting and clients -->
<section class="page spread-right">
  <p class="body-copy" style="left:16px;top:22px;width:248px">Our engagement doesn't stop at reports and advisory — we empower clients with ongoing access to the Continental Skills Academy's portfolio of certified training programmes, educational resources, and curated peer forums. This ensures that your leadership and operational teams are continuously upskilled to meet evolving resilience, compliance, and governance expectations.</p>

  <div class="dora">
    <div class="dora__org"><span class="dora__sq"></span><b>Veldt Bank</b>Steady Keel Framework Progress Tab</div>
    <p style="font-size:3.8px;color:var(--grey);margin-top:3px">Snapshot of maturity by pillar, with target tier and current score for each.</p>
    <div class="radars">
      <svg width="54" height="48" viewBox="0 0 54 48" role="img" aria-label="Radar chart of risk management maturity"><polygon points="27,4 49,20 41,44 13,44 5,20" fill="none" stroke="#ccc" stroke-width=".6"/><polygon points="27,14 40,22 34,38 18,36 14,22" fill="rgba(47,158,75,.5)" stroke="var(--green)" stroke-width=".6"/><polygon points="27,10 44,21 37,40 16,40 10,21" fill="none" stroke="var(--red)" stroke-width=".6"/></svg>
      <svg width="54" height="48" viewBox="0 0 54 48" role="img" aria-label="Radar chart of incident management maturity"><polygon points="27,4 49,20 41,44 13,44 5,20" fill="none" stroke="#ccc" stroke-width=".6"/><polygon points="27,12 42,22 32,36 20,38 12,20" fill="rgba(47,158,75,.45)" stroke="var(--green)" stroke-width=".6"/></svg>
      <svg width="54" height="48" viewBox="0 0 54 48" role="img" aria-label="Radar chart of resilience testing maturity"><polygon points="27,4 49,20 41,44 13,44 5,20" fill="none" stroke="#ccc" stroke-width=".6"/><polygon points="27,10 34,22 30,40 24,40 20,22" fill="rgba(224,189,46,.55)" stroke="var(--amber)" stroke-width=".6"/></svg>
      <svg width="54" height="48" viewBox="0 0 54 48" role="img" aria-label="Radar chart of third-party risk maturity"><polygon points="27,4 49,20 41,44 13,44 5,20" fill="none" stroke="#ccc" stroke-width=".6"/><polygon points="27,8 32,22 28,36 24,34 22,22" fill="rgba(208,18,27,.45)" stroke="var(--red)" stroke-width=".6"/></svg>
    </div>
    <span class="score" style="left:196px;top:74px">0.69</span>
    <span class="score" style="left:216px;top:74px;border-color:var(--red);background:#fde3e3">410.75</span>
  </div>

  <p class="body-copy" style="left:16px;top:172px">We provide scheduled, digestible reporting for leadership and regulators.</p>
  <div class="pill">We Work With Great Companies</div>
  <p class="body-copy" style="left:64px;top:206px">We support a diverse, global client base across regulated sectors.</p>

  <svg class="corner" width="280" height="120" viewBox="0 0 280 120" aria-hidden="true">
    <polygon points="0,40 40,120 0,120" fill="var(--ink)"/>
    <polygon points="280,0 280,40 240,40" fill="#7e8aa3" opacity=".6"/>
  </svg>
  <div class="clients">
    <span>Ferrowood</span><span>Dalmont</span><span>Kestrel Rock Capital</span><span>Lorimer Parts</span>
    <span>Oakleaf Life</span><span>Cabrin Finance</span><span>Ashbury Capital</span><span>Land Ledger Office</span>
    <span>Bank of Harrowgate</span><span>Allied Isle Bank</span><span>Skyvane Air</span><span>Lumen Health</span>
    <span>Verdant Produce</span><span>Sorrel Group</span><span>Pinecove Investments</span><span>Rochell Pharma</span>
    <span>Tonevia</span><span>Corvid Bank</span><span>Islay Life</span><span>Northmere Trust</span><span>Investra</span>
    <span>Westmark Lifeco</span><span>Ipsara</span><span>Avian Authority</span><span>Kinmore Credit Union</span><span>Debrook Stores</span>
  </div>
  <div class="page-num" style="right:14px">03</div>
</section>

<!-- Page 4: back cover -->
<section class="page back">
  <div class="brand"><span class="brand__mark"></span>DLO<span class="brand__divider"></span>HALCREST</div>
  <div class="contact">
    <p class="contact__title">Contact &amp; Next Steps</p>
    <p>If your organisation is navigating DORA, NIS2 or broader digital resilience obligations, let's talk.</p>
    <p><strong>We'd be delighted to arrange:</strong></p>
    <p>A tailored Halcrest demonstration | A technical deep dive with our advisors<br>A strategic review of your digital resilience priorities</p>
    <p style="margin-top:3px">info@dlorbis.ie | www.dlorbis.ie</p>
  </div>
</section>

</body>
</html>
```